Pebblesoft baby skincare

design business cards (double sided) and complimentary note (single sided)

Industry/Entity Type

Business

Colors

Designer to choose colors to be used in the design.

```html
<!DOCTYPE html>
<html lang="en">
<head>
<meta charset="utf-8">
<title>Pebblesoft baby skincare – business card</title>
<link href="https://fonts.googleapis.com/css2?family=Open+Sans:wght@400;600&display=swap" rel="stylesheet">
<style>
  :root {
    --backdrop: #eeeae3;
    --card: #ffffff;
    --gold: #c9aa55;
    --gold-light: #e2cd8a;
    --ink: #4a4a4a;
    --white: #ffffff;
  }
  * { margin: 0; padding: 0; box-sizing: border-box; }
  html, body {
    width: 1200px; height: 1024px; overflow: hidden;
    background: var(--backdrop);
    font-family: "Open Sans", Arial, sans-serif;
  }
  .canvas { position: relative; width: 1200px; height: 1024px; }
  .card {
    position: absolute; left: 240px;
    width: 720px; height: 411px;
    background: var(--card);
    box-shadow: 0 6px 18px rgba(0,0,0,0.12);
    overflow: hidden;
  }
  .card-front { top: 70px; }
  .card-back { top: 543px; }

  .wave { position: absolute; left: 0; top: 0; width: 720px; height: 411px; }

  .brand-name {
    position: absolute;
    font-weight: 400;
    color: var(--gold);
    line-height: 1;
    white-space: nowrap;
  }
  .card-front .brand-name { left: 48px; top: 92px; font-size: 58px; }

  .holder { position: absolute; left: 52px; top: 182px; }
  .holder-name { font-size: 22px; color: var(--gold); }
  .holder-role { font-size: 17px; color: var(--ink); margin-top: 2px; }

  .contacts {
    position: absolute; left: 392px; top: 104px;
    list-style: none;
  }
  .contacts li {
    display: flex; align-items: center; gap: 7px;
    font-size: 14px; color: var(--ink); margin-bottom: 5px;
    white-space: nowrap;
  }
  .contacts svg { width: 14px; height: 14px; flex: none; }

  .front-web {
    position: absolute; left: 40px; bottom: 20px;
    font-size: 17px; color: var(--white);
  }

  .card-back .brand-name {
    left: 0; right: 0; top: 150px; text-align: center; font-size: 84px;
  }
  .back-web {
    position: absolute; left: 40px; bottom: 34px;
    font-size: 19px; color: var(--ink);
  }
  .back-web .domain { color: var(--gold); }
</style>
</head>
<body>
<main class="canvas">

  <section class="card card-front" aria-label="Business card front">
    <svg class="wave" viewBox="0 0 720 411" aria-hidden="true">
      <path d="M0 300 C 250 330, 500 280, 640 190 C 690 155, 710 80, 720 20 L720 411 L0 411 Z" fill="var(--gold-light)"/>
      <path d="M0 330 C 250 360, 500 310, 640 220 C 690 185, 710 110, 720 50 L720 411 L0 411 Z" fill="var(--white)"/>
      <path d="M0 342 C 250 372, 500 322, 640 232 C 690 197, 710 122, 720 62 L720 411 L0 411 Z" fill="var(--gold)"/>
    </svg>

    <div class="brand-name">pebblesoft</div>

    <div class="holder">
      <div class="holder-name">Marlie Tenbrook</div>
      <div class="holder-role">CEO</div>
    </div>

    <ul class="contacts">
      <li>
        <svg viewBox="0 0 16 16" aria-hidden="true"><rect x="2" y="3" width="12" height="10" rx="1.5" fill="none" stroke="var(--gold)" stroke-width="1.6"/><rect x="5" y="6" width="6" height="2" fill="var(--gold)"/></svg>
        9410 2735
      </li>
      <li>
        <svg viewBox="0 0 16 16" aria-hidden="true"><path d="M4 2 L6.5 2 L7.5 5 L6 6.5 C6.8 8.3 7.7 9.2 9.5 10 L11 8.5 L14 9.5 L14 12 C14 13 13 14 12 14 C7 14 2 9 2 4 C2 3 3 2 4 2 Z" fill="var(--gold)"/></svg>
        0412 905 318
      </li>
      <li>
        <svg viewBox="0 0 16 16" aria-hidden="true"><rect x="1.5" y="3.5" width="13" height="9" fill="none" stroke="var(--gold)" stroke-width="1.6"/><path d="M1.5 3.5 L8 9 L14.5 3.5" fill="none" stroke="var(--gold)" stroke-width="1.6"/></svg>
        marlie@pebblesoftskincare.com
      </li>
    </ul>

    <div class="front-web">www.pebblesoftskincare.co</div>
  </section>

  <section class="card card-back" aria-label="Business card back">
    <div class="brand-name">pebblesoft</div>
    <div class="back-web">www.<span class="domain">pebblesoftskincare</span>.co</div>
  </section>

</main>
</body>
</html>
```